Personalized Technology Company Needs a Business Card

I need a double-sided business card. Both sides will have the logo, and the contact information. One side will be black, with the white / gray logo, and the other will be white, with the black / gray logo. The black side will have the text "Custom Gaming PC's" and will have a water-cooled gaming PC image. The white side will have the text "Custom Business Computers & Consulting", and will have a business / enterprise PC image. Feel free to add a conservative image in the background, while the color remains unchanged. I'm uploading the base logo (transparent), so you can modify the colors, both the finished colored logos and an idea of ​​the business card (with the current information, just missing the website, which is www.velmorisystems.com, please add it.) Thank you so much for your effort, I'll be specting your cool designs. Good Luck!

Target Market(s)

Gamers & Entrepreneurs / Business Owners / Chief Technology Officers

Industry/Entity Type

Technology Equipment

Contact Information for Business Card

I need a double-sided business card. Both sides will have the logo, and the contact information. One side will be black, with the white/gray logo, and the other one will be white, with the black/gray logo. The black side will have the text "Custom Gaming PC's" and will have a water-cooled gaming PC image. The white side will have the text "Custom Business Computers & Consulting", and will have a business/enterprise PC image. Feel free to add a conservative image in the background, whilst the color remains unchanged.

I'm uploading the base logo (transparent), so you can modify the colors, both the finished colored logos and an idea of the business card (with the actual information, just missing the website, which is www.velmorisystems.com, please add it.)

Thank you so much for your effort, I'll be specting your cool designs. Good Luck!

Font styles to use
Serif

Colors
000000
757575
ffffff

Requirements
Must have
• Please See Description
Nice to have
• Please See Description
Should not have
• Please See Description

```html
<!DOCTYPE html>
<html lang="en">
<head>
<meta charset="utf-8">
<title>Velmori Systems – Business Card</title>
<link rel="stylesheet" href="https://fonts.googleapis.com/css2?family=Roboto:wght@400;500;700&display=swap">
<style>
  :root {
    --stage: #2a2a2a;
    --ink: #0a0a0a;
    --paper: #ffffff;
    --taupe: #b9ada1;
    --grey: #757575;
    --light-grey: #e4e2de;
    --gaming-deep: #0b1650;
    --gaming-glow: #2a7be6;
    --office-light: #e8e6e2;
    --office-dark: #8d8882;
  }
  * { margin: 0; padding: 0; box-sizing: border-box; }
  html, body {
    width: 1200px; height: 800px; overflow: hidden;
    background: var(--stage);
    font-family: "Roboto", Arial, sans-serif;
  }
  .canvas { position: relative; width: 1200px; height: 800px; }
  .card {
    position: absolute; width: 600px; height: 340px;
    box-shadow: 0 18px 40px rgba(0,0,0,.55);
  }
  .card--dark  { left: 60px;  top: 50px; }
  .card--light { left: 540px; top: 420px; }
  .card svg { display: block; }
  .brand-name    { font-size: 30px; font-weight: 500; letter-spacing: 5px; }
  .brand-sub     { font-size: 9px;  font-weight: 500; letter-spacing: 4.2px; }
  .holder-name   { font-size: 19px; font-weight: 700; }
  .holder-role   { font-size: 14px; font-weight: 400; }
  .contact-line  { font-size: 15px; font-weight: 400; }
  .tagline       { font-size: 11.5px; font-weight: 400; }
  .card--dark .brand, .card--dark .contact-line { fill: var(--paper); }
  .card--light .brand, .card--light .contact-line { fill: var(--ink); }
</style>
</head>
<body>
<main class="canvas">

  <!-- Black side -->
  <section class="card card--dark" aria-label="Business card, black side">
    <svg width="600" height="340" viewBox="0 0 600 340">
      <defs>
        <linearGradient id="gamingGlow" x1="0" y1="0" x2="1" y2="1">
          <stop offset="0" stop-color="var(--gaming-deep)"/>
          <stop offset=".55" stop-color="var(--gaming-glow)"/>
          <stop offset="1" stop-color="var(--gaming-deep)"/>
        </linearGradient>
      </defs>
      <rect class="card-base" width="600" height="340" fill="var(--ink)"/>
      <polygon class="photo-edge" points="318,0 340,0 470,290 448,290" fill="var(--taupe)"/>
      <polygon class="photo-area" role="img" aria-label="Water-cooled custom gaming PC with blue lighting"
               points="340,0 600,0 600,290 470,290" fill="url(#gamingGlow)"/>
      <polygon class="name-bar" points="318,62 600,62 600,112 300,112" fill="var(--taupe)"/>
      <text class="holder-name" x="345" y="86" fill="var(--ink)">MARCO RUIZ TADEO</text>
      <text class="holder-role" x="345" y="104" fill="var(--ink)">CEO &amp; Co-Founder</text>

      <g class="brand">
        <circle cx="72" cy="110" r="16" fill="var(--grey)"/>
        <text class="brand-name" x="98" y="112">VELMORI</text>
        <text class="brand-sub" x="99" y="128">SYSTEMS</text>
      </g>

      <g class="contact-icons" fill="var(--taupe)">
        <circle cx="78" cy="182" r="13"/>
        <circle cx="78" cy="214" r="13"/>
        <circle cx="78" cy="246" r="13"/>
      </g>
      <g class="contact-glyphs" fill="none" stroke="var(--ink)" stroke-width="1.8" stroke-linecap="round">
        <path d="M72 176 q0 10 12 12 l2-3 -3-3 -2 1 q-3-2 -4-5 l1-2 -3-3 z" fill="var(--ink)" stroke="none"/>
        <rect x="73.5" y="206" width="9" height="16" rx="1.5"/>
        <rect x="70" y="240" width="16" height="11" rx="1"/>
        <path d="M70 241 l8 6 8-6"/>
      </g>
      <text class="contact-line" x="102" y="187">+52 5812 - 3047</text>
      <text class="contact-line" x="102" y="219">+52 55 - 4816 - 3390</text>
      <text class="contact-line" x="102" y="251">contact@velmorisystems.com</text>

      <polygon class="tagline-strip" points="300,268 600,268 600,290 300,290" fill="#cfc7bd"/>
      <text class="tagline" x="420" y="283" fill="var(--ink)">Custom Gaming PC's</text>
      <rect class="base-band" x="0" y="300" width="600" height="22" fill="var(--taupe)"/>
    </svg>
  </section>

  <!-- White side -->
  <section class="card card--light" aria-label="Business card, white side">
    <svg width="600" height="340" viewBox="0 0 600 340">
      <defs>
        <linearGradient id="officeTone" x1="0" y1="0" x2="1" y2="1">
          <stop offset="0" stop-color="var(--office-light)"/>
          <stop offset=".6" stop-color="#b9b5af"/>
          <stop offset="1" stop-color="var(--office-dark)"/>
        </linearGradient>
      </defs>
      <rect class="card-base" width="600" height="340" fill="var(--paper)"/>
      <polygon class="photo-edge" points="318,0 340,0 470,290 448,290" fill="var(--ink)"/>
      <polygon class="photo-area" role="img" aria-label="Business laptop showing a sales chart on an office desk"
               points="340,0 600,0 600,290 470,290" fill="url(#officeTone)"/>
      <polygon class="name-bar" points="318,62 600,62 600,112 300,112" fill="var(--ink)"/>
      <text class="holder-name" x="345" y="86" fill="var(--paper)">MARCO RUIZ TADEO</text>
      <text class="holder-role" x="345" y="104" fill="var(--paper)">CEO &amp; Co-Founder</text>

      <g class="brand">
        <circle cx="72" cy="110" r="16" fill="var(--grey)"/>
        <text class="brand-name" x="98" y="112">VELMORI</text>
        <text class="brand-sub" x="99" y="128">SYSTEMS</text>
      </g>

      <g class="contact-icons" fill="var(--ink)">
        <circle cx="78" cy="182" r="13"/>
        <circle cx="78" cy="214" r="13"/>
        <circle cx="78" cy="246" r="13"/>
      </g>
      <g class="contact-glyphs" fill="none" stroke="var(--paper)" stroke-width="1.8" stroke-linecap="round">
        <path d="M72 176 q0 10 12 12 l2-3 -3-3 -2 1 q-3-2 -4-5 l1-2 -3-3 z" fill="var(--paper)" stroke="none"/>
        <rect x="73.5" y="206" width="9" height="16" rx="1.5"/>
        <rect x="70" y="240" width="16" height="11" rx="1"/>
        <path d="M70 241 l8 6 8-6"/>
      </g>
      <text class="contact-line" x="102" y="187">+52 5812 - 3047</text>
      <text class="contact-line" x="102" y="219">+52 55 - 4816 - 3390</text>
      <text class="contact-line" x="102" y="251">contact@velmorisystems.com</text>

      <polygon class="tagline-strip" points="300,268 600,268 600,290 300,290" fill="var(--light-grey)"/>
      <text class="tagline" x="360" y="283" fill="var(--grey)">Custom Business Computers &amp; Consulting</text>
      <rect class="base-band" x="0" y="300" width="600" height="22" fill="var(--ink)"/>
    </svg>
  </section>

</main>
</body>
</html>
```